Business card required for IT Consultancy Business - Bluefern Consulting.
Company provides the whole nine yards of services across IT Architecture, design and execution.
Basically we provide consulting services to help businesses make sure their technology is enabling their business strategy.
Design for front and back required.
We would like the front of the card to inlcude:
Name
Title
Mobile number
email address
www.BFQ.com.au
Company logos attached.
Thank you
Industry/Entity Type
Business
Contact Information for Business Card
Name
Title
Mobile number
email address
www.BFQ.com.au
Look and feel
Each slider illustrates characteristics of the customer's brand and the style your logo design should communicate.

```html
<!DOCTYPE html>
<html lang="en">
<head>
<meta charset="utf-8">
<title>Bluefern Consulting – Business Card</title>
<link href="https://fonts.googleapis.com/css2?family=Arimo:wght@400;700&display=swap" rel="stylesheet">
<style>
  :root {
    --stage: #222222;
    --brand-blue: #1174bc;
    --brand-orange: #f05a28;
    --paper: #ffffff;
    --ink-grey: #666666;
    --on-blue: #ffffff;
  }
  * { box-sizing: border-box; margin: 0; padding: 0; }
  html, body {
    width: 1189px; height: 1200px; overflow: hidden;
    background: var(--stage);
    font-family: "Arimo", Arial, sans-serif;
  }
  .card {
    position: absolute; left: 171px; width: 856px; height: 488px;
    border-radius: 25px; overflow: hidden;
    box-shadow: 0 6px 8px rgba(0,0,0,.55);
  }
  .card--front { top: 67px; background: var(--brand-blue); }
  .card--back { top: 625px; background: var(--paper); }

  .wordmark {
    position: absolute; display: flex; align-items: center; gap: 16px;
    font-weight: 700; line-height: 1;
  }
  .wordmark__dot { width: 64px; height: 64px; border-radius: 50%; background: var(--brand-orange); flex: none; }
  .wordmark__name { font-size: 56px; letter-spacing: 1px; }
  .wordmark__name span { display: block; }
  .card--front .wordmark { left: 0; right: 0; top: 183px; justify-content: center; color: var(--on-blue); }
  .card--back .wordmark { right: 40px; top: 60px; color: var(--brand-blue); }
  .card--back .wordmark__name { font-size: 52px; text-align: left; }

  .front-url {
    position: absolute; left: 0; right: 0; top: 400px;
    text-align: center; color: var(--on-blue);
    font-size: 22px; line-height: 28px; letter-spacing: 5px;
  }

  .person { position: absolute; left: 39px; top: 266px; }
  .person__name { color: var(--brand-blue); font-weight: 700; font-size: 30px; line-height: 1; }
  .person__title { color: var(--brand-orange); font-size: 21px; line-height: 1; margin-top: 2px; }
  .divider { position: absolute; left: 247px; width: 570px; top: 312px; height: 1.5px; background: var(--brand-orange); }

  .contacts { position: absolute; left: 38px; top: 344px; list-style: none; }
  .contacts li { display: flex; align-items: center; gap: 8px; height: 30px; color: var(--ink-grey); font-size: 21px; }
  .contacts svg { width: 23px; height: 23px; flex: none; }

  .address { position: absolute; right: 39px; top: 350px; text-align: right; color: var(--ink-grey); font-size: 21px; line-height: 27px; font-style: normal; }
  .bands { position: absolute; left: 0; bottom: 0; width: 856px; height: 45px; }
</style>
</head>
<body>
  <section class="card card--front" aria-label="Card front">
    <div class="wordmark">
      <div class="wordmark__dot"></div>
      <div class="wordmark__name"><span>Bluefern</span><span>Consulting</span></div>
    </div>
    <p class="front-url">www.BFQ.com.au</p>
  </section>

  <section class="card card--back" aria-label="Card back">
    <div class="wordmark">
      <div class="wordmark__dot"></div>
      <div class="wordmark__name"><span>Bluefern</span><span>Consulting</span></div>
    </div>

    <div class="person">
      <p class="person__name">NORA WHITFIELD</p>
      <p class="person__title">Managing Director</p>
    </div>
    <div class="divider"></div>

    <ul class="contacts">
      <li>
        <svg viewBox="0 0 24 24" aria-hidden="true"><rect width="24" height="24" rx="3" fill="#1174bc"/><rect x="8" y="4" width="8" height="16" rx="1.5" fill="none" stroke="#fff" stroke-width="1.6"/><circle cx="12" cy="17" r="1" fill="#fff"/></svg>
        (02) 5550 1482
      </li>
      <li>
        <svg viewBox="0 0 24 24" aria-hidden="true"><rect width="24" height="24" rx="3" fill="#1174bc"/><rect x="4" y="7" width="16" height="11" fill="none" stroke="#fff" stroke-width="1.6"/><path d="M4 7l8 6 8-6" fill="none" stroke="#fff" stroke-width="1.6"/></svg>
        info@bluefernco.com
      </li>
      <li>
        <svg viewBox="0 0 24 24" aria-hidden="true"><rect width="24" height="24" rx="3" fill="#1174bc"/><g fill="none" stroke="#fff" stroke-width="1.3"><circle cx="12" cy="12" r="7"/><ellipse cx="12" cy="12" rx="3" ry="7"/><path d="M5 12h14M6 8.5h12M6 15.5h12"/></g></svg>
        www.BFQ.com.au
      </li>
    </ul>

    <address class="address">
      PO BOX 418<br>Level 3, Suite 7<br>14 Harbour Lane, Sydney
    </address>

    <svg class="bands" viewBox="0 0 856 45" preserveAspectRatio="none" aria-hidden="true">
      <path d="M0 9h535l-6 10H0z" fill="var(--brand-orange)"/>
      <path d="M0 24h532l16-23h308v44H0z" fill="var(--brand-blue)"/>
    </svg>
  </section>
</body>
</html>
```